Brain Science Music company needs modern clean website

We're looking for a website that's very clean and modern but also has some nice bold (futuristic) colors in it. The design should communicate a company that's providing something new and fresh! We'd greatly appreciate web designs similar to: https://thebrightfolio.co/

Lumen Cascade is a US-based Neuroscience music company that offers state-of-the-art technology solutions that help people focus, relax and sleep with the help of scientifically engineered music.

Target Market(s)

US businesses looking for specialized neuroscience music technology.

Logo Text

LumenCascade or LC

Coding

Coded - Design and coding required

Number of Pages Required

1 page

Font styles to use
Sans Serif

Colors

Designer to choose colors to be used in the design.

Requirements
Nice to have
• A website similar to: https://thebrightfolio.co/
We like the colors, the fonts, the simple design layouts and the colorful images.

```html
<!DOCTYPE html>
<html lang="en">
<head>
<meta charset="utf-8">
<title>LumenCascade — Music and the Brain</title>
<link href="https://fonts.googleapis.com/css2?family=Roboto:wght@400;500;700;900&display=swap" rel="stylesheet">
<style>
:root{
  --bg:#f5f5f5;
  --ink:#2b1199;
  --purple:#3a22a6;
  --purple-deep:#34129c;
  --cyan:#14bbe4;
  --text:#3b3b3b;
  --orange:#f59b1c;
  --sleep:#6c1aa8;
  --meditation:#c5124f;
  --athletics:#22a12b;
  --white:#ffffff;
}
*{box-sizing:border-box;margin:0;padding:0}
html,body{width:1200px;height:3162px;overflow:hidden}
body{background:var(--bg);font-family:"Roboto",Arial,sans-serif;color:var(--text);position:relative}
.abs{position:absolute}
.shapes{position:absolute;left:0;top:0;width:1200px;height:3162px}
.brand{font-weight:700;font-size:24px;color:var(--ink);letter-spacing:-0.3px}
.site-header .brand{left:150px;top:22px}
.nav{left:581px;top:26px;display:flex;align-items:center;gap:0}
.nav a{color:var(--white);text-decoration:none;font-size:13px;font-weight:500;margin-right:42px}
.nav a.contact{background:var(--cyan);border-radius:14px;padding:5px 18px;margin-right:0}
.hero-title{left:151px;top:180px;font-size:50px;font-weight:900;line-height:53px;color:var(--ink);letter-spacing:-0.3px}
.accent{color:var(--cyan)}
.hero-copy{left:150px;top:366px;width:360px;font-size:15px;line-height:22px}
.art{border-radius:50%}
.section-title{font-size:37px;font-weight:900;line-height:38px;color:var(--ink)}
.rule{height:5px;width:135px;background:var(--cyan)}
.feature-icon{width:37px;height:37px;border-radius:6px;display:flex;align-items:center;justify-content:center}
.feature-title{font-size:18px;font-weight:500}
.feature-copy{font-size:15px;line-height:22px;width:230px}
.right{text-align:right}
.entrain-title{color:var(--white)}
.step-num{font-size:36px;font-weight:700;color:var(--cyan)}
.step-copy{font-size:18px;line-height:22.5px;color:var(--white);width:330px}
.step-icon{width:78px;height:80px;border-radius:40%}
.story-intro{left:148px;top:2168px;width:900px;font-size:15px;line-height:22px}
.story-copy{left:593px;top:2280px;width:462px;font-size:15px;line-height:22px}
.story-copy p{margin-bottom:23px}
.footer-title{font-size:18px;font-weight:500;color:var(--white)}
.footer-copy{font-size:13.5px;line-height:22px;color:var(--white);width:440px}
.social{display:flex;gap:16px}
.social span{width:29px;height:29px;border-radius:50%;background:var(--white);display:block}
.divider{left:150px;top:3087px;width:900px;height:1px;background:var(--white)}
.copyright{left:0;width:1200px;top:3114px;text-align:center;font-size:13px;color:var(--white)}
</style>
</head>
<body>

<svg class="shapes" viewBox="0 0 1200 3162" aria-hidden="true">
  <!-- hero blob -->
  <path fill="var(--cyan)" d="M508,0 C488,70 520,150 508,230 C498,310 500,370 560,415 C640,470 700,500 770,525 C850,550 950,540 1040,535 C1110,532 1160,520 1200,505 L1200,0 Z"/>
  <path fill="var(--purple)" d="M530,0 C508,60 540,140 530,220 C520,300 515,355 565,395 C640,450 690,470 750,500 C820,530 900,525 980,520 C1070,515 1140,505 1200,480 L1200,0 Z"/>
  <!-- left blob -->
  <path fill="var(--cyan)" d="M0,302 C45,298 70,340 74,400 C78,470 100,512 134,545 C165,590 148,660 108,695 C76,720 35,712 0,708 Z"/>
  <path fill="var(--purple)" d="M0,312 C38,308 56,345 61,405 C66,470 86,515 118,545 C146,585 132,650 96,685 C66,712 30,702 0,700 Z"/>
  <!-- entrainment band -->
  <path fill="var(--cyan)" d="M0,1160 C90,1125 200,1120 280,1160 C360,1200 430,1230 530,1215 C650,1195 770,1165 890,1160 C1010,1155 1110,1150 1200,1140 L1200,1880 C1100,1870 1000,1830 900,1800 C780,1765 680,1800 560,1850 C480,1885 420,1900 350,1895 C250,1880 120,1810 0,1805 Z"/>
  <path fill="var(--purple)" d="M0,1165 C80,1130 190,1125 270,1170 C350,1215 420,1250 520,1245 C640,1235 760,1205 880,1195 C1000,1185 1100,1185 1200,1175 L1200,1880 C1100,1890 1000,1865 900,1835 C780,1800 680,1845 560,1885 C480,1912 420,1930 350,1922 C250,1908 120,1840 0,1835 Z"/>
  <!-- story blob -->
  <path fill="var(--cyan)" d="M0,2285 C80,2250 170,2250 240,2290 C320,2340 350,2430 362,2520 C372,2620 330,2720 240,2745 C150,2765 60,2730 0,2700 Z"/>
  <path fill="var(--purple-deep)" d="M0,2300 C70,2270 160,2268 225,2305 C300,2350 335,2430 345,2520 C355,2615 318,2705 235,2732 C150,2755 60,2720 0,2690 Z"/>
  <!-- footer wave -->
  <path fill="var(--cyan)" d="M0,2800 C150,2790 250,2830 380,2840 C520,2850 640,2830 780,2820 C920,2810 1050,2790 1200,2800 L1200,3162 L0,3162 Z"/>
  <path fill="var(--purple-deep)" d="M0,2860 C120,2840 220,2805 330,2808 C460,2812 560,2860 700,2865 C840,2870 960,2830 1080,2825 C1140,2822 1180,2835 1200,2845 L1200,3162 L0,3162 Z"/>
  <!-- feature connectors -->
  <polyline points="199,844 427,844 475,898" fill="none" stroke="var(--orange)" stroke-width="1"/>
  <polyline points="199,953 427,953 475,898" fill="none" stroke="var(--sleep)" stroke-width="1"/>
  <polyline points="1001,844 763,844 715,898" fill="none" stroke="var(--meditation)" stroke-width="1"/>
  <polyline points="1001,953 763,953 715,898" fill="none" stroke="var(--athletics)" stroke-width="1"/>
  <circle cx="475" cy="898" r="3" fill="var(--purple)"/>
  <circle cx="715" cy="898" r="3" fill="var(--purple)"/>
  <!-- story lines -->
  <rect x="906" y="2263" width="135" height="2" fill="var(--cyan)"/>
  <rect x="563" y="2546" width="2" height="135" fill="var(--cyan)"/>
</svg>

<header class="site-header">
  <div class="abs brand">LumenCascade</div>
  <nav class="abs nav">
    <a href="#">Home</a>
    <a href="#">Enhancing</a>
    <a href="#">Entrainment</a>
    <a href="#">Nolan’s Story</a>
    <a href="#" class="contact">Contact</a>
  </nav>
</header>

<section class="hero">
  <div class="abs art" role="img" aria-label="Glowing network brain illustration with floating music notes" style="left:655px;top:70px;width:340px;height:350px;background:radial-gradient(circle,#3fa8e6 0%,#3566cc 45%,rgba(58,34,166,0) 72%)"></div>
  <h1 class="abs hero-title">The new <span class="accent">FRONTIER</span><br>of <span class="accent">MUSIC</span> and<br>the <span class="accent">BRAIN</span></h1>
  <p class="abs hero-copy">Lorem ipsum dolor sit amet, consectetur adipiscing elit. Aenean ante eros, ullamcorper quis dignissim eget, volutpat</p>
</section>

<section class="enhancing">
  <h2 class="abs section-title" style="left:150px;top:660px">Merging <span class="accent">Neuroscience</span> and <span class="accent">Music</span>,<br>Creating audio <span class="accent">Enhancing</span></h2>
  <div class="abs rule" style="left:150px;top:761px"></div>

  <div class="abs feature-icon" style="left:150px;top:820px;background:var(--orange)"><svg width="20" height="20" viewBox="0 0 20 20"><circle cx="10" cy="10" r="6" fill="none" stroke="#fff" stroke-width="2.5" stroke-dasharray="3 2"/></svg></div>
  <div class="abs feature-title" style="left:199px;top:818px;color:var(--orange)">Productivity</div>
  <p class="abs feature-copy" style="left:199px;top:846px">Vivamus tincidunt nulla nec male-suada accumsan. Fusce lacinia, sapien ac</p>

  <div class="abs feature-icon" style="left:150px;top:930px;background:var(--sleep)"><svg width="20" height="20" viewBox="0 0 20 20"><path d="M13 3a7 7 0 1 0 4 11A6 6 0 0 1 13 3z" fill="#fff"/></svg></div>
  <div class="abs feature-title" style="left:199px;top:928px;color:var(--sleep)">Sleep</div>
  <p class="abs feature-copy" style="left:199px;top:957px">Vivamus tincidunt nulla nec male-suada accumsan. Fusce lacinia, sapien ac</p>

  <div class="abs art" role="img" aria-label="Cyan brain illustration" style="left:500px;top:820px;width:200px;height:220px;border-radius:48%;background:var(--cyan)"></div>

  <div class="abs feature-title right" style="left:791px;width:200px;top:818px;color:var(--meditation)">Meditation</div>
  <div class="abs feature-icon" style="left:1012px;top:820px;background:var(--meditation)"><svg width="20" height="20" viewBox="0 0 20 20"><circle cx="10" cy="5" r="2.5" fill="#fff"/><path d="M4 16 L10 9 L16 16 Z" fill="#fff"/></svg></div>
  <p class="abs feature-copy right" style="left:764px;top:846px">Vivamus tincidunt nulla nec male-suada accumsan. Fusce lacinia, sapien ac</p>

  <div class="abs feature-title right" style="left:791px;width:200px;top:928px;color:var(--athletics)">Athletics</div>
  <div class="abs feature-icon" style="left:1012px;top:930px;background:var(--athletics)"><svg width="20" height="20" viewBox="0 0 20 20"><circle cx="10" cy="4" r="2" fill="#fff"/><path d="M5 7 L10 9 L15 7 M10 9 L10 13 L6 18 M10 13 L14 18" stroke="#fff" stroke-width="2" fill="none"/></svg></div>
  <p class="abs feature-copy right" style="left:764px;top:957px">Vivamus tincidunt nulla nec male-suada accumsan. Fusce lacinia, sapien ac</p>
</section>

<section class="entrainment">
  <h2 class="abs section-title entrain-title" style="left:147px;top:1282px">Brainwave Entrainment</h2>
  <div class="abs rule" style="left:150px;top:1338px"></div>

  <div class="abs step-icon" role="img" aria-label="Brain with neural connections icon" style="left:150px;top:1412px;background:linear-gradient(90deg,var(--orange),var(--cyan))"></div>
  <div class="abs step-num" style="left:249px;top:1400px">01</div>
  <p class="abs step-copy" style="left:250px;top:1452px">Neurons in our brains communicate with each other, forming thoughts, emotions, and ideas using electrical impulses (commonly known as  Brainwaves).</p>

  <div class="abs step-icon" role="img" aria-label="Two-colour brain icon" style="left:610px;top:1408px;background:linear-gradient(90deg,var(--cyan),var(--orange))"></div>
  <div class="abs step-num" style="left:724px;top:1400px">02</div>
  <p class="abs step-copy" style="left:726px;top:1452px">Activities such as sleeping, working, or meditating, each have their own unique brainwave pattern.</p>

  <div class="abs step-icon" role="img" aria-label="Brain circuit icon" style="left:148px;top:1625px;background:linear-gradient(90deg,var(--orange),var(--cyan))"></div>
  <div class="abs step-num" style="left:248px;top:1616px">03</div>
  <p class="abs step-copy" style="left:250px;top:1668px">Lumen Cascade leverages Musical Phase Locking, to optimize  brainwave patterns for each desired activity.</p>

  <div class="abs step-icon" role="img" aria-label="Brain in a target circuit icon" style="left:610px;top:1625px;background:radial-gradient(circle,var(--cyan) 0%,var(--orange) 55%,rgba(245,155,28,0) 70%)"></div>
  <div class="abs step-num" style="left:725px;top:1618px">04</div>
  <p class="abs step-copy" style="left:729px;top:1670px">Our music is driven by science. We utilize large scale studies and data  from electroencephlograms to produce substantial results.</p>
</section>

<section class="story">
  <h2 class="abs section-title" style="left:147px;top:2068px">Nolan’s <span class="accent">Story</span></h2>
  <div class="abs rule" style="left:148px;top:2121px"></div>
  <p class="abs story-intro">Founder and Team Leader of Lumen Cascade, in conjunction with  primary scientific advisor Dr. Elliot Marsh. Nolan is a pioneer in the neuroscience of music, and key innovator on the technology of Musical Phase Locking.</p>

  <div class="abs" role="img" aria-label="Open book illustration with flying books and swirling light" style="left:160px;top:2258px;width:380px;height:356px;border-radius:30%;background:radial-gradient(ellipse at 50% 60%,#f4ecd4 0%,#c9c7f0 40%,rgba(52,18,156,0) 72%)"></div>

  <div class="abs story-copy">
    <p>At the age of 10, Nolan wrote his first symphony and began studying music composition</p>
    <p>After exposure to alpha waves in music, Nolan began a lifelong pursuit of merging neuroscience and music composition</p>
    <p>Nolan founded Clearwave Corp in 2003, creating audio workstations for those who wanted to experience the effects of music guided by neuroscience, as well as software for brain-computer interfaces.</p>
    <p>As the science progressed and Clearwave Corp grew, Nolan decided to form Mindtune.io in 2014, a website and app that allowed nearly anybody to access the music, not just those who were scientifically minded</p>
    <p>Lumen Cascade was formed to further the vision of neuroscience-based music becoming a daily resource that everyone should experience.</p>
  </div>
</section>

<footer class="site-footer">
  <div class="abs brand" style="left:150px;top:2955px;color:var(--white)">LumenCascade</div>
  <div class="abs footer-title" style="left:382px;top:2958px">About us</div>
  <p class="abs footer-copy" style="left:382px;top:2985px">massa dolor, finibus non cursus dapibus, ultrices a nisl. Cras maximus bibendum eros, non rutrum arcu bibendum nec. Etiam quis orci leo. Class aptent taciti sociosqu ad litora torquent per conubia</p>
  <div class="abs footer-title" style="left:885px;top:2958px">About us</div>
  <div class="abs social" style="left:885px;top:2988px"><span></span><span></span><span></span><span></span></div>
  <div class="abs divider"></div>
  <div class="abs copyright">©  All CopyRights are reserved</div>
</footer>

</body>
</html>
```